THE PRACTICE NAME "The Renal Crest MD" FOR A NEW MEDICAL PRACTICE STARTUP

THIS IS A BUSINESS CARD REQUEST FOR A KIDNEY DOCTOR's(NEPHROLOGIST) PRACTICE, THIS PRACTICE WILL BE IN EL PASO,TEXAS USA.OPEN TO INNOVATIVE IDEAS!

THE RENAL CREST MD ( NAME OF PRACTICE)

VIKRANT L. MOTHRE, MD FNKF FASN ( NAME OF PHYSICIAN WITH DEGREES)
BOARD CERTIFIED INTERNAL MEDICINE
BOARD CERTIFIED NEPHROLOGY
HYPERTENSION SPECIALIST

OFFICE ADDRESS, PHONE, FAX AND EMAIL PENDING

Guarding Health. Building Futures.(MOTTO) THE LOGO SHOILD REFLECT THIS MESSAGE. WE NEED A LOGO DESIGN WITH 2 KIDNEYS OR CAN BE ONE KIDNEY ALSO.

Target Market(s)

PATIENTS WITH KIDNEY DISEASE, HYPERTENSION, ENGLISH AND SPANISH SPEAKING POPULATION AND PATIENTS ON DIALYSIS

Industry/Entity Type

Health Care

Contact Information for Business Card

HYPERTENSION SPECIALIST

WEBSITE URL PENDING

Font styles to use
Serif
Sans Serif
Script

Colors
fbed38
ffc214
fbf289
fbee3e
5c5c5c
333333
1b1b1b
757575
d3d3d3

Requirements
Must have
• A KIDNEY LOGO
• NAME OF THE PRACTICE
Nice to have
• IF THE CARD CAN BE IN THE SHAPE OF A KIDNEY

```html
<!DOCTYPE html>
<html lang="en">
<head>
<meta charset="UTF-8">
<title>The Renal Crest MD — Business Card</title>
<link rel="stylesheet" href="https://fonts.googleapis.com/css2?family=Source+Sans+3:wght@400;600;700&display=swap">
<style>
  :root {
    --backdrop: #e9e7e3;
    --card-light: #ffffff;
    --card-silver: #dcdcdc;
    --maroon: #6a1b1d;
    --gold: #f4b11a;
    --gold-deep: #e39a05;
    --ink: #2b2b2b;
    --ink-soft: #333333;
    --icon: #6a1b1d;
  }
  * { box-sizing: border-box; margin: 0; padding: 0; }
  html, body { width: 1200px; height: 900px; overflow: hidden; }
  body {
    background: var(--backdrop);
    font-family: "Source Sans 3", sans-serif;
    color: var(--ink);
  }
  .business-card {
    position: absolute;
    left: 150px; top: 190px;
    width: 900px; height: 520px;
    border-radius: 44px;
    overflow: hidden;
    background: linear-gradient(160deg, var(--card-light) 0%, #f1f1f1 45%, var(--card-silver) 100%);
    box-shadow: 0 14px 34px rgba(0,0,0,0.18);
  }
  .brand {
    position: absolute;
    left: 0; right: 0; top: 38px;
    display: flex; flex-direction: column; align-items: center;
    padding-left: 110px;
  }
  .brand-mark {
    width: 46px; height: 46px; border-radius: 50%;
    background: var(--gold);
    margin-bottom: 10px;
  }
  .brand-name {
    font-weight: 700;
    font-size: 34px;
    letter-spacing: 1px;
    color: var(--maroon);
  }
  .physician {
    position: absolute;
    right: 470px; top: 178px;
    text-align: right;
  }
  .physician-name {
    font-weight: 700; font-size: 25px; color: var(--maroon);
    margin-bottom: 4px;
  }
  .credential {
    font-size: 21px; line-height: 1.2; color: var(--ink-soft);
  }
  .physician-email {
    position: absolute;
    right: 470px; top: 372px;
    font-size: 23px; color: var(--ink);
  }
  .contact-list {
    position: absolute;
    left: 470px; top: 184px;
    list-style: none;
  }
  .contact-item {
    display: flex; align-items: flex-start;
    font-size: 23px; line-height: 1.2; color: var(--ink);
  }
  .contact-icon { width: 22px; height: 22px; margin: 3px 20px 0 0; flex: none; }
  .contact-item.address { margin-bottom: 6px; }
  .contact-item.empty { height: 30px; }
  .tagline-band {
    position: absolute;
    left: 0; right: 0; bottom: 0; height: 108px;
    background: linear-gradient(180deg, var(--gold) 0%, var(--gold-deep) 100%);
    display: flex; align-items: center; justify-content: center;
  }
  .tagline {
    font-weight: 700; font-size: 40px; color: var(--maroon);
    letter-spacing: 0.3px;
  }
</style>
</head>
<body>
  <article class="business-card">
    <header class="brand">
      <span class="brand-mark"></span>
      <span class="brand-name">THE RENAL CREST MD</span>
    </header>

    <section class="physician">
      <p class="physician-name">Vikrant L. Mothre, MD FNKF FASN</p>
      <p class="credential">Board Certified Internal Medicine</p>
      <p class="credential">Board Certified Nephrology</p>
      <p class="credential">Hypertension Specialist</p>
    </section>
    <p class="physician-email">vikrant@renalcrestmd.com</p>

    <ul class="contact-list">
      <li class="contact-item address">
        <svg class="contact-icon" viewBox="0 0 24 24"><path fill="var(--icon)" d="M12 1a8 8 0 0 0-8 8c0 6 8 14 8 14s8-8 8-14a8 8 0 0 0-8-8zm0 11a3 3 0 1 1 0-6 3 3 0 0 1 0 6z"/></svg>
        <span>4210 Mesa Verde Blvd.<br>Suite 208<br>El Paso, TX 79912</span>
      </li>
      <li class="contact-item phone">
        <svg class="contact-icon" viewBox="0 0 24 24"><circle cx="12" cy="12" r="11" fill="var(--icon)"/><path fill="#fff" d="M9 6c1 0 1.5 2.5 1 3l-1 1c.7 1.8 2.2 3.3 4 4l1-1c.5-.5 3 0 3 1s-1 3-3 3c-4 0-8-4-8-8 0-2 2-3 3-3z"/></svg>
        <span>915.555.0142</span>
      </li>
      <li class="contact-item fax">
        <svg class="contact-icon" viewBox="0 0 24 24"><rect x="7" y="2" width="10" height="7" fill="none" stroke="var(--icon)" stroke-width="2"/><rect x="2" y="9" width="20" height="12" rx="2" fill="var(--icon)"/><rect x="6" y="13" width="8" height="2" fill="#fff"/><rect x="16" y="12" width="3" height="3" fill="#fff"/></svg>
        <span>915.555.0143</span>
      </li>
      <li class="contact-item empty">
        <svg class="contact-icon" viewBox="0 0 24 24"><rect x="2" y="5" width="20" height="14" rx="1" fill="var(--icon)"/><path d="M3 6l9 7 9-7" fill="none" stroke="#fff" stroke-width="1.6"/></svg>
      </li>
      <li class="contact-item web">
        <svg class="contact-icon" viewBox="0 0 24 24" fill="none" stroke="var(--icon)" stroke-width="1.6"><circle cx="12" cy="12" r="10"/><ellipse cx="12" cy="12" rx="4.5" ry="10"/><path d="M2 12h20M4 7h16M4 17h16"/></svg>
        <span>www.renalcrestmd.com</span>
      </li>
    </ul>

    <footer class="tagline-band">
      <p class="tagline">Guarding Health. Building Futures</p>
    </footer>
  </article>
</body>
</html>
```